Specialist Doctor Personal Website

I wanted a website:
1. In my name
2. Describing my scope of practice
3. Having my photo
4. Has links to the places I work at
5. Provides patient information
6. Provides an email for contact

Target Market(s)

Victorian patients and GPs

Industry/Entity Type

Health

Coding

Coded - Design and coding required

Number of Pages Required

1 page

Font styles to use
Script

Colors
0054AA
0677BA
7BADD7
CADEEF
E8F1F8
6B429C
8869AF
B7A5CE
E3DAEB
F3F0F8

Requirements
Must have
• Modern design
Nice to have
• Links to email/fax/linkedin

```html
<!DOCTYPE html>
<html lang="en">
<head>
<meta charset="utf-8">
<title>Specialist Doctor</title>
<link href="https://fonts.googleapis.com/css2?family=Poppins:ital,wght@0,400;0,500;0,600;0,700;1,400&display=swap" rel="stylesheet">
<style>
:root{
  --blue:#1a9ad6;
  --blue-deep:#0677BA;
  --team-blue:#3a97cc;
  --ink:#2b2b2b;
  --muted:#555;
  --paper:#f4f3f1;
  --dark:#414345;
  --form-dark:#3b4046;
  --star:#f2c22b;
  --white:#fff;
}
*{box-sizing:border-box;margin:0;padding:0}
html,body{width:1200px;height:4758px;overflow:hidden}
body{font-family:'Poppins',sans-serif;color:var(--ink);position:relative;background:var(--white)}
.abs{position:absolute}
section,header,footer{position:absolute;left:0;width:1200px}
.btn{position:absolute;display:flex;align-items:center;justify-content:center;font-size:14px;font-weight:500;text-transform:uppercase}
.btn-blue{background:var(--blue);color:var(--white)}
.center{text-align:center;left:0;width:1200px}

/* hero */
.hero{top:0;height:675px;background:linear-gradient(135deg,#b9a391 0%,#d8c7b8 40%,#e9e4de 70%,#c9c0b6 100%)}
.hero-shade{position:absolute;inset:0;background:rgba(60,45,35,.35)}
.brand{left:44px;top:20px;color:var(--white);font-size:32px;font-weight:500;line-height:1}
.brand small{display:block;font-size:20px;font-weight:400;margin-top:4px}
.nav{left:428px;top:55px;display:flex;gap:0;color:var(--white);font-size:13px}
.nav span{padding:0 17px;border-right:1px solid rgba(255,255,255,.8);line-height:14px}
.nav span:last-child{border:none}
.btn-appt{left:976px;top:42px;width:163px;height:38px;background:var(--white);color:var(--ink);font-size:14px}
.hero h1{top:237px;color:var(--white);font-size:52px;font-weight:600;line-height:62px}
.hero p{top:395px;left:335px;width:530px;text-align:center;color:var(--white);font-size:15px;line-height:19px}
.btn-services{left:543px;top:488px;width:112px;height:44px;border:2px solid var(--white);color:var(--white);text-transform:none;font-size:15px}

/* about */
.about{top:675px;height:478px;background:var(--paper)}
.about-photo{left:128px;top:93px;width:340px;height:340px;border-radius:50%;border:6px solid var(--white);box-shadow:0 4px 14px rgba(0,0,0,.25);background:radial-gradient(circle at 50% 40%,#e9e9e9,#c9cdd4 60%,#28416e 100%)}
.about h2{left:570px;top:150px;font-size:34px;font-weight:500;color:var(--blue)}
.about p{left:570px;top:218px;width:480px;font-size:14.5px;line-height:28px;color:var(--muted)}
.about .btn{left:571px;top:350px;width:124px;height:37px}

/* services */
.services{top:1153px;height:852px}
.section-title{font-size:34px;font-weight:500;color:var(--blue)}
.services h2{top:83px}
.services .lead{top:160px;left:270px;width:660px;text-align:center;font-size:14.5px;line-height:19px;color:var(--ink)}
.card{position:absolute;top:257px;width:324px;height:435px;background:var(--white);box-shadow:0 3px 8px rgba(0,0,0,.18)}
.card-img{height:272px;position:relative}
.card-label{position:absolute;left:0;bottom:0;width:100%;height:42px;background:rgba(8,100,130,.85);color:var(--white);font-size:17px;font-weight:500;display:flex;align-items:center;justify-content:center}
.card p{margin:16px 22px 0;text-align:center;font-size:14px;line-height:19px;color:var(--muted)}
.card .btn{left:96px;top:372px;width:112px;height:32px;font-size:13px}
.card .btn-outline{background:var(--white);color:var(--blue);border:2px solid var(--blue)}
.dots{top:762px;left:564px;display:flex;gap:8px}
.dots i{width:13px;height:13px;border-radius:50%;background:var(--blue);display:block}
.dots i.off{background:var(--white);border:2px solid var(--blue)}

/* stats */
.stats{top:2005px;height:280px;background:var(--paper)}
.stat{position:absolute;top:98px;width:240px;text-align:center}
.stat b{display:block;font-size:52px;font-weight:500;color:var(--blue);line-height:60px}
.stat span{display:block;font-size:15px;font-weight:500;margin-top:10px}

/* testimonial */
.testimonial{top:2366px;height:624px;background:linear-gradient(90deg,#c9d2dc 0%,#e4e6e8 30%,#eceae6 60%,#d4d8de 100%)}
.testimonial-veil{position:absolute;inset:0;background:rgba(235,240,246,.55)}
.testimonial h2{top:54px;font-weight:500}
.avatar{left:523px;top:170px;width:170px;height:170px;border-radius:50%;border:4px solid var(--white);background:radial-gradient(circle at 50% 45%,#f4ede8,#c6a995 60%,#6b4e3f 100%)}
.arrow{position:absolute;top:325px;width:40px;height:40px}
.quote{top:358px;left:190px;width:820px;text-align:center;font-size:19px;font-weight:500;line-height:30px;color:#111}
.qm{color:var(--blue);font-size:44px;font-weight:700;line-height:0;vertical-align:-12px}
.author{top:472px;font-size:27px;font-weight:500;color:var(--blue)}
.stars{top:518px;left:540px;display:flex;gap:10px}

/* team */
.team{top:2990px;height:525px;background:var(--team-blue)}
.team h2{top:100px;color:var(--white);font-size:34px;font-weight:500}
.team .lead{top:166px;left:260px;width:680px;text-align:center;color:var(--white);font-size:13px;line-height:24px}
.member{position:absolute;top:3280px;width:232px;height:325px}
.member-hover{background:rgba(110,170,225,.85);color:var(--white);text-align:center}
.member-hover h3{margin-top:96px;font-size:17px;font-weight:500}
.member-hover .role{font-size:12px;opacity:.8;margin-top:2px}
.member-social{display:flex;justify-content:center;gap:9px;margin-top:16px}
.member-social i{width:24px;height:24px;background:var(--blue);display:block;border-radius:3px}
.member-hover .erm{font-size:12.5px;margin-top:18px}
.btn-more{left:527px;top:3667px;width:145px;height:36px;background:var(--blue);color:var(--white);font-size:13px;text-transform:none}

/* cta */
.cta{top:3757px;height:558px;background:linear-gradient(90deg,#2eb2e6 0%,#1f8ed3 45%,#1d7fcb 100%)}
.cta h2{left:92px;top:150px;width:600px;color:var(--white);font-size:35px;font-weight:500;line-height:43px}
.cta p{left:88px;top:307px;width:620px;color:var(--white);font-size:18.5px;line-height:35px}
.form{position:absolute;left:778px;top:3676px;width:317px;height:517px;background:var(--form-dark);box-shadow:0 6px 16px rgba(0,0,0,.35);border-radius:3px}
.form h3{position:absolute;left:31px;top:65px;color:var(--white);font-size:23px;font-weight:500}
.form .note{position:absolute;left:31px;top:101px;color:#c7c9cc;font-size:13px;font-style:italic}
.field{position:absolute;left:31px;width:256px;height:34px;background:var(--white);border-radius:2px;font-size:11px;color:#999;display:flex;align-items:center;padding:0 11px;justify-content:space-between}
.field svg{width:10px;height:10px}
.form .btn{left:34px;top:405px;width:146px;height:34px;font-size:11.5px}

/* footer */
.footer{top:4315px;height:443px;background:var(--dark);color:var(--white)}
.footer h2{top:57px;color:var(--blue);font-size:33px;font-weight:500}
.footer .rule{left:520px;top:111px;width:160px;height:2px;background:var(--white)}
.footer h4{top:148px;font-size:17px;font-weight:500}
.fnav{top:195px;left:363px;display:flex;font-size:13px}
.fnav span{padding:0 21px;border-right:1px solid var(--white);line-height:14px}
.fnav span:last-child{border:none}
.footer .signup{top:262px;font-size:14.5px;font-weight:500}
.news-input{left:386px;top:300px;width:334px;height:42px;background:var(--white);color:#888;font-size:13px;display:flex;align-items:center;padding:0 10px}
.news-btn{left:720px;top:300px;width:116px;height:42px;font-size:14px}
.social{top:368px;left:561px;display:flex;gap:7px}
.social i{width:19px;height:19px;border-radius:50%;background:var(--blue);display:block}
.footer .line{left:0;top:407px;width:1200px;height:1px;background:#9a9a9a}
.copy{top:418px;font-size:15px}
</style>
</head>
<body>

<header class="hero">
  <div class="abs" role="img" aria-label="Photograph of a doctor holding a patient's hands" style="inset:0"></div>
  <div class="hero-shade"></div>
  <div class="abs brand">Specialist<small>Doctor</small></div>
  <nav class="abs nav"><span>HOME</span><span>ABOUT US</span><span>BLOG</span><span>SERVICES</span><span>CONTACT US</span></nav>
  <div class="btn btn-appt">GET APPOINTMENT</div>
  <h1 class="abs center">Welcome to Specialist<br>Doctor</h1>
  <p class="abs">I am a Psychologist offering psychotherapy for individuals and couples, and clinical consultation and training and education for mental and medical health professionals and agencies.</p>
  <div class="btn btn-services">My Services</div>
</header>

<section class="about">
  <div class="abs about-photo" role="img" aria-label="Portrait photograph of the doctor"></div>
  <h2 class="abs">About us</h2>
  <p class="abs">Lorem ipsum dolor sit amet, consectetur adipiscing elit, sed do eiusmod tempor incididunt ut labore et dolore magna aliqua. Quis ipsum suspendisse ultrices gravida. Risus commodo viverra maecenas accumsan lacus vel facilisis.</p>
  <div class="btn btn-blue">READ MORE</div>
</section>

<section class="services">
  <h2 class="abs center section-title">Our Services</h2>
  <p class="abs lead">Lorem ipsum dolor sit amet, consectetur adipiscing elit. Vivamus lacinia odio vitae vestibulum vestibulum.</p>
  <div class="card" style="left:53px">
    <div class="card-img" role="img" aria-label="Photograph of a physiotherapy session" style="background:linear-gradient(160deg,#e8eef2,#b8c4cc 55%,#3d6f8e)"><div class="card-label">Service</div></div>
    <p>Lorem ipsum dolor sit amet, consectetur adipiscing elit, sed do eiQuis ipsum suspendisse ultrices gravida.</p>
    <div class="btn btn-blue">READ MORE</div>
  </div>
  <div class="card" style="left:441px">
    <div class="card-img" role="img" aria-label="Photograph of a group counselling session" style="background:linear-gradient(160deg,#efe9e2,#c9b8a6 55%,#4e5e6a)"><div class="card-label">Service I</div></div>
    <p>Lorem ipsum dolor sit amet, consectetur adipiscing elit, sed do eiQuis ipsum suspendisse ultrices gravida.</p>
    <div class="btn btn-outline">READ MORE</div>
  </div>
  <div class="card" style="left:823px">
    <div class="card-img" role="img" aria-label="Photograph of a doctor taking notes with a patient" style="background:linear-gradient(160deg,#7d9466,#3f4a3a 55%,#1f2a2e)"><div class="card-label">Service 2</div></div>
    <p>Lorem ipsum dolor sit amet, consectetur adipiscing elit, sed do eiQuis ipsum suspendisse ultrices gravida.</p>
    <div class="btn btn-blue">READ MORE</div>
  </div>
  <div class="abs dots"><i></i><i class="off"></i><i></i></div>
</section>

<section class="stats">
  <div class="stat" style="left:72px"><b>500+</b><span>Satisfied Patients</span></div>
  <div class="stat" style="left:328px"><b>260+</b><span>M.B.B.S Doctor</span></div>
  <div class="stat" style="left:586px"><b>816+</b><span>Successful Patient</span></div>
  <div class="stat" style="left:842px"><b>240+</b><span>Successfull Surgeries</span></div>
</section>

<section class="testimonial">
  <div class="abs" role="img" aria-label="Faded photograph of patients in a waiting room" style="inset:0"></div>
  <div class="testimonial-veil"></div>
  <h2 class="abs center section-title">What Patient Says</h2>
  <div class="abs avatar" role="img" aria-label="Portrait photograph of the patient"></div>
  <svg class="arrow" style="left:50px" viewBox="0 0 40 40"><circle cx="20" cy="20" r="19" fill="#1a9ad6"/><path d="M23 12l-8 8 8 8" stroke="#fff" stroke-width="2" fill="none"/></svg>
  <svg class="arrow" style="left:1128px" viewBox="0 0 40 40"><circle cx="20" cy="20" r="19" fill="#1a9ad6"/><path d="M17 12l8 8-8 8" stroke="#fff" stroke-width="2" fill="none"/></svg>
  <p class="abs quote"><span class="qm">&ldquo;</span> Lorem ipsum dolor sit amet, consectetur adipiscing elit, sed do eiusmod tempor incididunt ut labore et dolore magna aliqua. Quis ipsum suspendisse ultrices gravida. Risus commodo viverra maecenas accumsan lacus vel facilisis. <span class="qm">&rdquo;</span></p>
  <div class="abs center author">- Marla Quinton</div>
  <div class="abs stars">
    <svg width="16" height="16" viewBox="0 0 24 24"><path fill="#f2c22b" d="M12 2l3 7 7 .6-5.3 4.6 1.7 7.3L12 17.8 5.6 21.5l1.7-7.3L2 9.6 9 9z"/></svg>
    <svg width="16" height="16" viewBox="0 0 24 24"><path fill="#f2c22b" d="M12 2l3 7 7 .6-5.3 4.6 1.7 7.3L12 17.8 5.6 21.5l1.7-7.3L2 9.6 9 9z"/></svg>
    <svg width="16" height="16" viewBox="0 0 24 24"><path fill="#f2c22b" d="M12 2l3 7 7 .6-5.3 4.6 1.7 7.3L12 17.8 5.6 21.5l1.7-7.3L2 9.6 9 9z"/></svg>
    <svg width="16" height="16" viewBox="0 0 24 24"><path fill="#f2c22b" d="M12 2l3 7 7 .6-5.3 4.6 1.7 7.3L12 17.8 5.6 21.5l1.7-7.3L2 9.6 9 9z"/></svg>
    <svg width="16" height="16" viewBox="0 0 24 24"><path fill="#f2c22b" d="M12 2l3 7 7 .6-5.3 4.6 1.7 7.3L12 17.8 5.6 21.5l1.7-7.3L2 9.6 9 9z"/></svg>
  </div>
</section>

<section class="team">
  <h2 class="abs center">Our team membar</h2>
  <p class="abs lead">Lorem ipsum dolor sit amet, consectetur adipiscing elit, sed do eiusmod tempor incididun labore etdolore magna aliqua. Ut enim ad minim veniam,</p>
</section>
<div class="member" role="img" aria-label="Photograph of a female doctor with stethoscope" style="left:97px;background:linear-gradient(180deg,#e6e8ea,#c9ccd0 60%,#4c6e96)"></div>
<div class="member member-hover" style="left:354px">
  <h3>Dr. Elena Varro</h3>
  <div class="role">Neurologist</div>
  <div class="member-social"><i></i><i></i><i></i><i></i></div>
  <div class="erm">ERM: +000 555 010 200</div>
</div>
<div class="member" role="img" aria-label="Photograph of a female doctor in a white coat" style="left:612px;background:linear-gradient(180deg,#d8d4cf,#b9b2ab 60%,#f1f1f1)"></div>
<div class="member" role="img" aria-label="Photograph of a male doctor with glasses" style="left:869px;background:linear-gradient(180deg,#3c4048,#7f8590 50%,#ebecee)"></div>
<div class="btn btn-more">Membar more II</div>

<section class="cta">
  <div class="abs" role="img" aria-label="Faded photograph of a smiling doctor" style="inset:0"></div>
  <h2 class="abs">Some of your questions are very serious for us feel free ask our any time?</h2>
  <p class="abs">Lorem ipsum dolor sit amet, consectetur adipiscing elit, sed do eiusmod tempor incididunt ut labore et dolore magna aliqua. Quis ipsum suspendisse ultrices gravida. Risus commodo viverra maecenas accumsan lacus vel facilisis.</p>
</section>

<div class="form">
  <h3>GET APPOINTMENT</h3>
  <div class="note">Clinic health are available 24/7</div>
  <div class="field" style="top:142px">New Patient*<svg viewBox="0 0 10 10"><path d="M2 3l3 3 3-3" stroke="#666" fill="none"/></svg></div>
  <div class="field" style="top:195px">Your Name*</div>
  <div class="field" style="top:248px">Patient Date*<svg viewBox="0 0 10 10"><path d="M2 3l3 3 3-3" stroke="#666" fill="none"/></svg></div>
  <div class="field" style="top:301px">Email or Phone*<span>@example.com</span></div>
  <div class="field" style="top:354px">Patient Gender*<svg viewBox="0 0 10 10"><path d="M2 3l3 3 3-3" stroke="#666" fill="none"/></svg></div>
  <div class="btn btn-blue">SUBMIT REQUEST &rarr;</div>
</div>

<footer class="footer">
  <h2 class="abs center">Specialist Doctor</h2>
  <div class="abs rule"></div>
  <h4 class="abs center">QUICK LINK</h4>
  <nav class="abs fnav"><span>HOME</span><span>ABOUT US</span><span>BLOG</span><span>SERVICES</span><span>CONTACT US</span></nav>
  <div class="abs center signup">Sign Up To Receive Our Newsletter</div>
  <div class="abs news-input">Email Here</div>
  <div class="btn btn-blue news-btn">SUBSCRIBE</div>
  <div class="abs social"><i></i><i></i><i></i><i></i></div>
  <div class="abs line"></div>
  <div class="abs center copy">Copyright &copy; 2023 . All rights reserved</div>
</footer>

</body>
</html>
```